E-commerce Website needs category banner

What we need for our category banner is a clean, predominately black design that showcases the product we are trying to sell (currently only 1), and a few subtle gradients that follow the pattern set by previous designs.

An example will be provided to showcase what we want.

It needs to say:
Outdoor Motion Detection Lighting in large, clear font similar to the example provided.

Please ensure dimensions are as follows: 980x300

Target Market(s)

Senior citizens, businesses, homeowners, families, etc

Industry/Entity Type

Product

Font styles to use
Sans Serif

Requirements
Must have
• It needs to say:
Outdoor Motion Detection Lighting in large, clear font similar to the example provided
980x300 is the required size!
Should not have
• Too much going on- clean and simple please (no crazy fonts, logos, etc)

```html
<!DOCTYPE html>
<html lang="en">
<head>
<meta charset="utf-8">
<title>Outdoor Motion Detection Lighting</title>
<link rel="stylesheet" href="https://fonts.googleapis.com/css2?family=Open+Sans:wght@700&display=swap">
<style>
  :root {
    --bg: #1c1d1f;
    --text: #ffffff;
    --product-light: #4b5459;
    --product-mid: #33393d;
    --product-dark: #1f2427;
    --glow: rgba(255, 255, 255, 0.55);
  }
  html, body {
    margin: 0;
    padding: 0;
    width: 1200px;
    height: 469px;
    overflow: hidden;
    background: var(--bg);
  }
  .banner {
    position: relative;
    width: 1200px;
    height: 469px;
    background: var(--bg);
    overflow: hidden;
  }
  .banner__headline {
    position: absolute;
    left: 80px;
    top: 136px;
    margin: 0;
    font-family: "Open Sans", Arial, sans-serif;
    font-weight: 700;
    font-size: 71px;
    line-height: 89px;
    letter-spacing: -0.5px;
    color: var(--text);
    text-transform: uppercase;
    white-space: nowrap;
    transform: scaleX(0.95);
    transform-origin: left top;
  }
  .banner__product {
    position: absolute;
    left: 806px;
    top: 34px;
    width: 292px;
    height: 386px;
    border-radius: 48% 48% 46% 46% / 40% 40% 58% 58%;
    background:
      radial-gradient(ellipse 60% 45% at 35% 30%, var(--product-light) 0%, transparent 70%),
      linear-gradient(160deg, var(--product-mid) 0%, var(--product-dark) 100%);
    box-shadow:
      0 0 18px 6px var(--glow),
      0 0 45px 14px rgba(255, 255, 255, 0.18);
  }
</style>
</head>
<body>
  <div class="banner">
    <h1 class="banner__headline">Outdoor Motion<br>Detection Lighting</h1>
    <div class="banner__product" role="img" aria-label="Product photo: dark grey wireless LED motion-sensor spotlight on a swivel wall mount, with a soft white glow around it"></div>
  </div>
</body>
</html>
```